BRASKETT LAND SERVICES BILLBOARD DESIGN

I NEED A BILLBOARD FOR MY BUSINESS. WE ARE A LAND CLEARING COMPANY AND I WOULD LIKE TO ADD A PICTURE OF MY TRACK LOADER TO THE SIGN. OPEN TO COLORS. I WOULD ALSO LIKE TO HAVE MY PHONE NUMBER 555-284-7196, WEBSITE WWW.BRASKETTLANDSERVICES.EXAMPLE, AND EMAIL ON THE SIGN (CONTACT@BRASKETTLANDSERVICES.EXAMPLE). DESIGNERS CAN HAVE THE FREEDOM TO DO WHATEVER STYLE THEY WANT AND TO USE ANY COLORS THEY WANT.

Target Market(s)

ANYONE WITH PROPERTY

Requirements
Must have
• PICTURE OF TRACK LOADER, WEBSITE, PHONE NUMBER, EMAIL
Nice to have
• OPEN TO ANYTHING
Should not have
• OPEN TO ANYTHING

```html
<!DOCTYPE html>
<html lang="en">
<head>
<meta charset="utf-8">
<title>Braskett Land Services Billboard</title>
<link href="https://fonts.googleapis.com/css2?family=Anton&display=swap" rel="stylesheet">
<style>
  :root {
    --ink: #0f0f0f;
    --charcoal: #2b2b2b;
    --white: #ffffff;
    --orange: #f0621f;
    --orange-deep: #c9420f;
    --page: #e9e9e9;
  }
  html, body {
    margin: 0;
    padding: 0;
    width: 1039px;
    height: 1200px;
    overflow: hidden;
    background: var(--page);
  }
  .canvas {
    position: relative;
    width: 1039px;
    height: 1200px;
  }
  .billboard {
    position: absolute;
    left: 0;
    top: 340px;
    width: 1108px;
    height: 555px;
    transform: scale(0.9377);
    transform-origin: 0 0;
    background: var(--ink);
    overflow: hidden;
    font-family: "Anton", "Oswald", sans-serif;
  }
  .billboard__art {
    position: absolute;
    inset: 0;
  }
  .brand {
    position: absolute;
    left: 45px;
    margin: 0;
    font-weight: 400;
    text-transform: uppercase;
    line-height: 1;
    letter-spacing: 0.5px;
  }
  .brand__line1 {
    top: 52px;
    font-size: 70px;
    color: var(--ink);
  }
  .brand__line2 {
    top: 138px;
    font-size: 76px;
    color: var(--white);
  }
  .call-sign {
    position: absolute;
    left: 78px;
    top: 250px;
    width: 312px;
    height: 178px;
    box-sizing: border-box;
    border: 9px solid var(--orange);
    border-radius: 12px;
    background: linear-gradient(180deg, #ffffff 0%, #e4e8ee 100%);
    box-shadow: 0 0 0 2px #8a2b08, 4px 6px 10px rgba(0,0,0,0.5);
    transform: rotate(-4deg);
    text-align: center;
    color: var(--ink);
  }
  .call-sign__cta {
    display: block;
    margin-top: 14px;
    font-size: 62px;
    line-height: 1;
  }
  .call-sign__phone {
    display: block;
    font-size: 46px;
    line-height: 1.1;
  }
  .contact {
    position: absolute;
    left: 40px;
    top: 476px;
    line-height: 1;
  }
  .contact__email {
    display: block;
    font-size: 22px;
    color: var(--white);
    letter-spacing: 0.3px;
  }
  .contact__web {
    display: block;
    margin-top: 8px;
    font-size: 29px;
    color: var(--ink);
    letter-spacing: 0.3px;
  }
</style>
</head>
<body>
<div class="canvas">
  <section class="billboard">
    <svg class="billboard__art" width="1108" height="555" viewBox="0 0 1108 555" aria-hidden="false">
      <defs>
        <linearGradient id="woodsDark" x1="0" y1="0" x2="1" y2="1">
          <stop offset="0" stop-color="#3a3a38"/>
          <stop offset="0.5" stop-color="#242422"/>
          <stop offset="1" stop-color="#121212"/>
        </linearGradient>
        <linearGradient id="titleBand" x1="0" y1="0" x2="1" y2="0">
          <stop offset="0" stop-color="#ffffff"/>
          <stop offset="0.75" stop-color="#ffffff" stop-opacity="0.85"/>
          <stop offset="1" stop-color="#ffffff" stop-opacity="0"/>
        </linearGradient>
        <linearGradient id="loaderPhoto" x1="0" y1="0" x2="0" y2="1">
          <stop offset="0" stop-color="#7d8b55"/>
          <stop offset="0.35" stop-color="#4f6a2c"/>
          <stop offset="0.6" stop-color="#a4653a"/>
          <stop offset="0.8" stop-color="#8b8d6a"/>
          <stop offset="1" stop-color="#b7a877"/>
        </linearGradient>
        <linearGradient id="orangeBand" x1="0" y1="0" x2="1" y2="0">
          <stop offset="0" stop-color="#f37a2c"/>
          <stop offset="1" stop-color="#c9420f"/>
        </linearGradient>
      </defs>

      <rect class="woods-backdrop" x="0" y="0" width="600" height="470" fill="url(#woodsDark)"
            role="img" aria-label="Dark faded photo of wooded land behind the headline"/>

      <rect class="title-band" x="0" y="45" width="540" height="92" fill="url(#titleBand)"/>

      <polygon class="loader-photo" points="592,0 1108,0 1108,500 640,500 472,250"
               fill="url(#loaderPhoto)" role="img"
               aria-label="Photo of an orange tracked loader with a forestry mulcher head in a wooded lot"/>

      <path class="photo-frame" d="M572 -5 L450 250 L618 512" fill="none" stroke="#ffffff" stroke-width="14"/>
      <path class="photo-frame-inner" d="M592 0 L472 250 L640 500 L1108 500" fill="none" stroke="#0f0f0f" stroke-width="6"/>

      <polygon class="contact-band" points="0,468 600,468 556,555 0,555" fill="url(#orangeBand)"/>

      <g class="corner-stripes" fill="#f0621f">
        <polygon points="955,522 990,522 975,555 940,555"/>
        <polygon points="1000,522 1035,522 1020,555 985,555"/>
        <polygon points="1045,522 1108,522 1108,555 1030,555"/>
      </g>

      <g class="sign-strings" stroke="#7f8a96" stroke-width="3" fill="none">
        <line x1="228" y1="187" x2="135" y2="268"/>
        <line x1="228" y1="187" x2="306" y2="260"/>
      </g>
      <circle class="sign-nail" cx="228" cy="187" r="7" fill="#d9262c" stroke="#ffffff" stroke-width="2"/>
    </svg>

    <h1 class="brand brand__line1">BRASKETT LAND</h1>
    <p class="brand brand__line2">SERVICES</p>

    <div class="call-sign">
      <span class="call-sign__cta">CALL NOW!</span>
      <span class="call-sign__phone">555-284-7196</span>
    </div>

    <div class="contact">
      <span class="contact__email">CONTACT@BRASKETTLANDSERVICES.EXAMPLE</span>
      <span class="contact__web">WWW.BRASKETTLANDSERVICES.EXAMPLE</span>
    </div>
  </section>
</div>
</body>
</html>
```